Sweet Bag Packaging Design

I need a Sweet Bag designing that looks modern and will appeal to Kids and adults. The bag will be aimed at families. The bag needs to have a clear window on the front of the bag so the product can be seen. Also need a logo on the front of the bag.
Back of pack will have area for Ingredients.
Reason: Would like to see more designs before I decide.
Target Market(s)
Families (Needs to aim at kids and adults)
Industry/Entity Type
Product
Requirements
Must have
- Clear window on the from of the bag.
Need a logo designing for the front of bag fo KL Confectionery.
Please use the template provided for the final design. Other ways of presentation with be ok for the intial design stage.
The design needs to be generic as the packaging will be used to pack lots of different sweets and the variety of sweet will be overprinted on the front.
Nice to have
- May be nice to have some characters on the design.
The front needs a Price flash (Wow £1)

```html
<!DOCTYPE html>
<html lang="en">
<head>
<meta charset="utf-8">
<title>Sugar Buttons – Sweet Bag Front</title>
<link rel="stylesheet" href="https://fonts.googleapis.com/css2?family=Alfa+Slab+One&family=Arimo:wght@700&family=Open+Sans:wght@300&display=swap">
<style>
  :root {
    --bag-purple-top: #5b3f8c;
    --bag-navy-bottom: #2c4490;
    --frame-pink: #c67aab;
    --title-green: #a9c22c;
    --title-yellow: #f6e43c;
    --price-navy: #2a3a88;
    --sky-blue: #c8e2f5;
    --cloud-edge: #7cbde6;
    --cloud-white: #ffffff;
    --brand-pink: #f2b6d8;
    --note-green: #a8c030;
    --rule-grey: #333333;
    --page: #ffffff;
  }
  html, body {
    margin: 0;
    padding: 0;
    width: 1096px;
    height: 1200px;
    overflow: hidden;
    background: var(--page);
  }
  .artboard { display: block; width: 1096px; height: 1200px; }
  .title-text {
    font-family: "Alfa Slab One", serif;
    fill: var(--cloud-white);
    font-size: 54px;
  }
  .brand-name {
    font-family: "Alfa Slab One", serif;
    fill: var(--brand-pink);
    font-size: 28px;
  }
  .price-amount, .price-word {
    font-family: "Alfa Slab One", serif;
    fill: var(--price-navy);
  }
  .price-amount { font-size: 100px; }
  .price-word { font-size: 52px; }
  .weight-text {
    font-family: "Arimo", sans-serif;
    font-weight: 700;
    font-size: 31px;
    fill: var(--price-navy);
  }
  .note-text {
    font-family: "Open Sans", sans-serif;
    font-weight: 300;
    font-size: 23px;
    fill: var(--note-green);
  }
  .note-line { stroke: var(--note-green); stroke-width: 1; }
</style>
</head>
<body>
<svg class="artboard" viewBox="0 0 1096 1200" xmlns="http://www.w3.org/2000/svg">
  <defs>
    <linearGradient id="bagBackground" x1="0" y1="0" x2="0" y2="1">
      <stop offset="0" stop-color="var(--bag-purple-top)"/>
      <stop offset="0.45" stop-color="#3a4490"/>
      <stop offset="1" stop-color="var(--bag-navy-bottom)"/>
    </linearGradient>
    <linearGradient id="skyScene" x1="0" y1="0" x2="0" y2="1">
      <stop offset="0" stop-color="var(--sky-blue)"/>
      <stop offset="0.45" stop-color="#e4f1fb"/>
      <stop offset="1" stop-color="var(--cloud-white)"/>
    </linearGradient>
    <clipPath id="bagClip"><rect x="218" y="78" width="627" height="1097"/></clipPath>
  </defs>

  <line class="page-rule" x1="0" y1="12" x2="1096" y2="12" stroke="var(--rule-grey)" stroke-width="1.5"/>

  <g class="bag-front" clip-path="url(#bagClip)">
    <rect class="bag-background" x="218" y="78" width="627" height="1097" fill="url(#bagBackground)"/>

    <rect class="sky-cloud-top" x="645" y="108" width="215" height="220" rx="80" fill="var(--sky-blue)"
          role="img" aria-label="Soft pale blue cloud illustration"/>

    <rect class="cloud-scene" x="218" y="540" width="627" height="560" rx="60" fill="url(#skyScene)"
          role="img" aria-label="Cloud landscape with a rainbow and a fairy-tale castle surrounding the clear window"/>

    <rect class="pack-frame" x="252" y="119" width="568" height="991" rx="24"
          fill="none" stroke="var(--frame-pink)" stroke-width="9"/>

    <rect class="price-flash" x="222" y="548" width="270" height="222" rx="70"
          fill="var(--cloud-white)" stroke="var(--cloud-edge)" stroke-width="5"/>
    <text class="price-amount" x="278" y="668">£1</text>
    <text class="price-word" x="276" y="723">value</text>

    <g class="brand-mark">
      <circle cx="312" cy="275" r="9" fill="var(--brand-pink)"/>
      <text class="brand-name" x="330" y="285">KL Confectionery</text>
    </g>

    <rect class="product-title-box" x="283" y="360" width="510" height="150" rx="18"
          fill="var(--title-green)" stroke="var(--title-yellow)" stroke-width="6"/>
    <text class="title-text" x="538" y="464" text-anchor="middle"
          transform="translate(538 464) scale(1 1.25) translate(-538 -464)">Sugar Buttons</text>

    <ellipse class="weight-badge" cx="557" cy="1110" rx="71" ry="36" fill="var(--title-green)"/>
    <text class="weight-text" x="557" y="1121" text-anchor="middle">350g</text>
  </g>
  <rect class="bag-outline" x="218" y="78" width="627" height="1097" fill="none" stroke="#222" stroke-width="1.5"/>

  <g class="annotations">
    <line class="note-line" x1="827" y1="713" x2="890" y2="713"/>
    <text class="note-text" x="897" y="716">white</text>
    <text class="note-text" x="897" y="747">clouds</text>

    <line class="note-line" x1="646" y1="870" x2="894" y2="870"/>
    <text class="note-text" x="899" y="873">clear</text>
    <text class="note-text" x="899" y="904">window</text>

    <line class="note-line" x1="795" y1="1062" x2="890" y2="1062"/>
    <text class="note-text" x="899" y="1065">white</text>
    <text class="note-text" x="899" y="1096">clouds</text>
  </g>
</svg>
</body>
</html>
```